Business card for exciting VC company

Should look simple, crisp, and modern.

Industry/Entity Type

Venture Capital

Contact Information for Business Card

Would like to see at least one design that has our blue on the back with the tagline "Transforming Traditional Industry" and white front with contact details.

Font styles to use
Sans Serif

Requirements
Must have
• Logo

Gregory Tallis
gtallis@brindlewave.vc
Managing Partner
M (628)354-xxxx

```html
<!DOCTYPE html>
<html lang="en">
<head>
<meta charset="utf-8">
<title>Brindlewave Capital – Business Card</title>
<link href="https://fonts.googleapis.com/css2?family=Montserrat:wght@400;600&display=swap" rel="stylesheet">
<style>
  :root {
    --backdrop: #d4d8d9;
    --card: #f1f1ef;
    --ink: #141414;
    --blue: #2f7fd6;
    --grey: #4a4a4a;
  }
  * { margin: 0; padding: 0; box-sizing: border-box; }
  html, body { width: 1200px; height: 852px; overflow: hidden; }
  body {
    background: var(--backdrop);
    font-family: "Montserrat", sans-serif;
    display: flex;
    align-items: center;
    justify-content: center;
    gap: 60px;
  }
  .card {
    width: 520px;
    height: 297px;
    background: var(--card);
    box-shadow: 0 10px 28px rgba(0,0,0,0.12);
    position: relative;
  }
  .brand {
    color: var(--ink);
    font-weight: 600;
    text-transform: uppercase;
    line-height: 1;
    text-align: center;
  }
  .brand__name { display: block; letter-spacing: 0.04em; }
  .brand__sub { display: block; letter-spacing: 0.45em; margin-top: 8px; }

  /* Front */
  .card--front .brand {
    position: absolute;
    left: 28px;
    top: 126px;
    width: 200px;
  }
  .card--front .brand__name { font-size: 24px; }
  .card--front .brand__sub { font-size: 10px; }
  .divider {
    position: absolute;
    left: 250px;
    top: 92px;
    width: 2px;
    height: 112px;
    background: var(--blue);
  }
  .contact {
    position: absolute;
    left: 278px;
    top: 106px;
    color: var(--grey);
    font-size: 13px;
    line-height: 1.45;
  }
  .contact__name {
    color: var(--blue);
    font-weight: 600;
    font-size: 14px;
    text-transform: uppercase;
    letter-spacing: 0.03em;
  }
  .contact__title { margin-bottom: 8px; }
  .contact__line { display: flex; align-items: center; gap: 8px; }
  .contact__line svg { width: 11px; height: 11px; flex: none; }

  /* Back */
  .card--back {
    display: flex;
    align-items: center;
    justify-content: center;
  }
  .card--back .brand__name { font-size: 40px; }
  .card--back .brand__sub { font-size: 15px; margin-top: 12px; }
</style>
</head>
<body>
  <section class="card card--front">
    <div class="brand">
      <span class="brand__name">Brindlewave</span>
      <span class="brand__sub">Capital</span>
    </div>
    <div class="divider"></div>
    <div class="contact">
      <p class="contact__name">Gregory Tallis</p>
      <p class="contact__title">Managing Partner</p>
      <p class="contact__line">
        <svg viewBox="0 0 12 12" aria-hidden="true"><path d="M3 1 L5 3.5 L4 5 Q5 7 7 8 L8.5 7 L11 9 L9.5 11 Q5 11 2.5 8 Q0.5 5 1 2.5 Z" fill="var(--blue)"/></svg>
        (628)354-xxxx
      </p>
      <p class="contact__line">
        <svg viewBox="0 0 12 12" aria-hidden="true"><rect x="0.75" y="2.25" width="10.5" height="7.5" fill="none" stroke="var(--blue)" stroke-width="1.2"/><path d="M0.75 2.5 L6 6.5 L11.25 2.5" fill="none" stroke="var(--blue)" stroke-width="1.2"/></svg>
        gtallis@brindlewave.vc
      </p>
    </div>
  </section>

  <section class="card card--back">
    <div class="brand">
      <span class="brand__name">Brindlewave</span>
      <span class="brand__sub">Capital</span>
    </div>
  </section>
</body>
</html>
```